UPDATE: Web Page: Keystone Public Relations

i DON'T NEED PICTURES, JUST SOMETHING CLEAN LIKE THE ARTWORK ATTACHED OR BUILT ON BUSINESS CARDS...PLEASE DESIGN AROUND THAT.

I need a clean webpage for new public relations firm that I will launch on March 1st. I HAVE JUST ADDED BUSINESS CARD MODELS FOR WEB PAGE COVER AND START IN TERMS OF DESIGN.

Pull down categories: (built on this model: http://www.wendelmorrowpr.com/contact/)

-Home
-Services
-Expertise
-About Us
-Press
-Contact

Marcus Telfer, CEO
Keystone Public Relations
2875 West Maple Ave.
Los Angeles CA 90012
(o) 213.555.0142
(f) 213.555.0187
marcus@keystonekpr.com

Target Market(s)

Pacifica Assembly House, Halvern Civic Hall
Lobbying type services to government/public affairs

Industry/Entity Type

Business

Number of Pages Required

4 page

Requirements
Must have
• Portray a beautiful picture of LA City or a government hall way (not domes)
• 1. Public Relations---Pic of Advocacy
• 2. Public Affairs--pick of government capitol Sacramento/Halvern Civic Hall
• 3. Strategy & Advisory Services--Something smart like chalk board.
Nice to have
• Great Pics on slider pages
Should not have
• Assembly House Dome (California)
• Halvern Civic Hall

```html
<!DOCTYPE html>
<html lang="en">
<head>
<meta charset="utf-8">
<title>Keystone Public Relations</title>
<link href="https://fonts.googleapis.com/css2?family=Open+Sans:wght@400;600;700&display=swap" rel="stylesheet">
<style>
:root{
  --blue:#1e9be0;
  --header:#141414;
  --panel:#2b2b2b;
  --deep:#1d1d1d;
  --text:#a9a9a9;
  --muted:#7a7a7a;
  --white:#ffffff;
  --rule:#444;
}
*{box-sizing:border-box;margin:0;padding:0}
html,body{width:869px;height:1200px;overflow:hidden}
body{font-family:"Open Sans",Arial,sans-serif;background:var(--deep);color:var(--text);position:relative}
.section{position:absolute;left:0;width:869px}
.wrap{position:absolute;left:72px;width:725px}

/* header */
.site-header{top:0;height:87px;background:var(--header)}
.brand{position:absolute;left:72px;top:14px;display:flex;align-items:center;gap:8px}
.brand-mark{width:46px;height:46px;border-radius:50%;background:var(--blue)}
.brand-name{font-size:24px;font-weight:600;color:var(--blue);line-height:1}
.brand-name small{display:block;font-size:6px;letter-spacing:1.6px;margin-top:3px;text-transform:uppercase}
.search{position:absolute;left:669px;top:18px;width:127px;height:22px;background:#5a5a5a;color:#ccc;font-size:7.5px;padding:6px 7px}
.search svg{position:absolute;right:6px;top:5px}
.nav{position:absolute;top:55px;right:73px;display:flex;gap:25px;list-style:none;font-size:9px;color:#b5b5b5}
.nav .active{color:var(--white)}

/* hero */
.hero{top:87px;height:298px;background:radial-gradient(ellipse at 50% 30%,#4f6075 0%,#2a3544 55%,#151b24 100%)}
.hero-arrow{position:absolute;top:141px}

/* welcome */
.welcome{top:385px;height:155px;background:var(--panel);text-align:center}
h2{font-weight:600;color:var(--blue)}
.welcome h2{font-size:21px;margin-top:30px}
.welcome p{width:590px;margin:7px auto 0;font-size:8.6px;line-height:16.2px}

/* services */
.services{top:540px;height:261px;background:var(--deep);text-align:center}
.services h2{font-size:21px;margin-top:17px}
.card{position:absolute;top:58px;width:165px}
.card-img{height:96px}
.card-cap{position:relative;height:39px;background:#efefef;color:var(--blue);font-size:10.4px;line-height:39px}
.card-cap::before{content:"";position:absolute;left:74px;top:-8px;border:8px solid transparent;border-top:0;border-bottom-color:#efefef}
.card p{font-size:7.4px;line-height:12.4px;color:var(--muted);margin-top:7px}

/* press */
.press{top:801px;height:184px;background:var(--panel)}
.press h2{position:absolute;left:72px;top:30px;font-size:17px}
.press-nav{position:absolute;left:778px;top:38px;font-size:7px;color:#555;letter-spacing:3px}
.rule{position:absolute;left:72px;width:725px;height:1px;background:var(--rule)}
.item{position:absolute;top:70px;width:170px}
.badge{position:absolute;left:0;top:0;width:38px;height:38px;border-radius:50%;background:#555;color:var(--white);text-align:center;font-size:8.5px;line-height:9px;padding-top:9px}
.badge b{display:block;font-size:13px;font-weight:400;line-height:14px}
.item-body{position:absolute;left:45px;top:2px;width:120px}
.item-body h3{font-size:9px;font-weight:400;color:var(--white);line-height:11px}
.item-body p{font-size:7.4px;color:var(--muted);line-height:11.2px;margin-top:5px}
.vsep{position:absolute;top:68px;width:1px;height:72px;background:var(--rule)}

/* footer */
.footer{top:985px;height:149px;background:var(--deep)}
.col{position:absolute;top:24px}
.col h4{font-size:13px;font-weight:400;color:var(--white)}
.col p{font-size:7.4px;line-height:12.4px;color:var(--muted);margin-top:8px}
.col a{color:var(--muted)}
.fsep{position:absolute;top:22px;width:1px;height:118px;background:#3a3a3a}
.links{list-style:none;font-size:7.2px;line-height:12.4px;color:#999;margin-top:8px}
.links li::before{content:"· "}
.email{position:relative;width:113px;height:20px;margin-top:8px;background:var(--white);font-size:7px;color:#555;padding:6px 7px}
.email span{position:absolute;right:0;top:0;width:26px;height:20px;background:#ccc}
.email svg{position:absolute;left:9px;top:5px}
.social{display:flex;gap:12px;margin-top:13px}
.social i{width:10px;height:10px;background:#ddd}
.social i+i{background:#666;border-radius:50%}

/* bottom bar */
.bottom{top:1134px;height:66px;background:var(--header);font-size:7.4px;color:#8a8a8a}
.bottom p{position:absolute;left:72px}
.bottom-icons{position:absolute;left:750px;top:24px;display:flex;gap:5px}
</style>
</head>
<body>

<header class="section site-header">
  <div class="brand">
    <span class="brand-mark"></span>
    <div class="brand-name">Keystone<small>Public Relations</small></div>
  </div>
  <div class="search">Search
    <svg width="10" height="10" viewBox="0 0 10 10"><circle cx="4" cy="4" r="3" fill="none" stroke="#ddd" stroke-width="1.4"/><path d="M6.2 6.2 9 9" stroke="#ddd" stroke-width="1.4"/></svg>
  </div>
  <ul class="nav">
    <li class="active">Home</li><li>Services</li><li>Expertise</li><li>About Us</li><li>Press</li><li>Contact</li>
  </ul>
</header>

<section class="section hero" role="img" aria-label="Team of business people in suits standing before a world map">
  <svg class="hero-arrow" style="left:22px" width="14" height="14" viewBox="0 0 14 14"><path d="M10 2 4 7l6 5" fill="none" stroke="#fff" stroke-width="3"/></svg>
  <svg class="hero-arrow" style="left:833px" width="14" height="14" viewBox="0 0 14 14"><path d="M4 2l6 5-6 5" fill="none" stroke="#fff" stroke-width="3"/></svg>
</section>

<section class="section welcome">
  <h2>Welcome to Keystone PR</h2>
  <p>Aenean sed quam non sapien faucibus consequat vitae sit amet orci. Praesent quis risus mi. In mollis nulla in pulvinar dictum. Vivamus interdum sagittis felis, ut dapibus ligula feugiat ac. In dictum sapien eu tellus finibus fermentum. Aenean faucibus lacus ut mollis commodo. Donec vestibulum odio sem, ac laoreet massa ullamcorper id. Donec molestie nisi et tellus hendrerit vehicula. Nunc eu ligula sed quam pulvinar maximus in vitae eros. Proin porta fermentum ipsum, vel porttitor turpis venenatis luctus.</p>
</section>

<section class="section services">
  <h2>Our Services</h2>
  <div class="card" style="left:72px">
    <div class="card-img" role="img" aria-label="Red loudspeakers on a pole against a hazy sky" style="background:linear-gradient(135deg,#cfc7a0,#8e8a78)"></div>
    <div class="card-cap">Aliquam erat</div>
    <p>Integer eu massa lacinia, lacinia nulla non, volutpat purus. Sed libero felis, vestibulum et dolor eget, lacinia aliquet neque.</p>
  </div>
  <div class="card" style="left:258px">
    <div class="card-img" role="img" aria-label="Hand holding wooden blocks with contact icons" style="background:linear-gradient(135deg,#2a2f5a,#6a5a78)"></div>
    <div class="card-cap">Proin a dolor</div>
    <p>Integer eu massa lacinia, lacinia nulla non, volutpat purus. Sed libero felis, vestibulum et dolor eget, lacinia aliquet neque.</p>
  </div>
  <div class="card" style="left:445px">
    <div class="card-img" role="img" aria-label="Phone screen showing social media apps" style="background:linear-gradient(135deg,#3a8ee0,#1b4fa8)"></div>
    <div class="card-cap">Vestibulum ante</div>
    <p>Integer eu massa lacinia, lacinia nulla non, volutpat purus. Sed libero felis, vestibulum et dolor eget, lacinia aliquet neque.</p>
  </div>
  <div class="card" style="left:631px">
    <div class="card-img" role="img" aria-label="Glowing network of connected people icons" style="background:linear-gradient(135deg,#1a3a8a,#3aa0e0)"></div>
    <div class="card-cap">Nunc sit amet</div>
    <p>Integer eu massa lacinia, lacinia nulla non, volutpat purus. Sed libero felis, vestibulum et dolor eget, lacinia aliquet neque.</p>
  </div>
</section>

<section class="section press">
  <h2>Press Release</h2>
  <div class="press-nav">◀▶</div>
  <div class="rule" style="top:55px"></div>
  <article class="item" style="left:72px"><div class="badge">Feb<b>23</b></div><div class="item-body"><h3>Donec molestie nisi et tellus hendrerit</h3><p>Proin porta fermentum ipsum, vel porttitor turpis venenatis luctus<br>Feb 23, 2015</p></div></article>
  <div class="vsep" style="left:241px"></div>
  <article class="item" style="left:260px"><div class="badge">Feb<b>23</b></div><div class="item-body"><h3>Donec molestie nisi et tellus hendrerit</h3><p>Proin porta fermentum ipsum, vel porttitor turpis venenatis luctus<br>Feb 23, 2015</p></div></article>
  <div class="vsep" style="left:434px"></div>
  <article class="item" style="left:453px"><div class="badge">Feb<b>23</b></div><div class="item-body"><h3>Donec molestie nisi et tellus hendrerit</h3><p>Proin porta fermentum ipsum, vel porttitor turpis venenatis luctus<br>Feb 23, 2015</p></div></article>
  <div class="vsep" style="left:622px"></div>
  <article class="item" style="left:642px"><div class="badge">Feb<b>23</b></div><div class="item-body"><h3>Donec molestie nisi et tellus hendrerit</h3><p>Proin porta fermentum ipsum, vel porttitor turpis venenatis luctus<br>Feb 23, 2015</p></div></article>
  <div class="rule" style="top:152px"></div>
</section>

<footer class="section footer">
  <div class="col" style="left:72px;width:210px">
    <h4>About us</h4>
    <p>Sed nec enim tempus, porta mi ut, auctor neque. Aliquam ut velit ac nibh vestibulum laoreet. Cras condimentum ut ligula eget rhoncus. In sit amet odio consequat, lobortis neque quis. Nam et tortor in ante iaculis porttitor in luctus mi. Vivamus gravida sem a pretium euismod. Nam lobortis, purus et fringilla tempus.</p>
  </div>
  <div class="fsep" style="left:295px"></div>
  <div class="col" style="left:315px;width:220px">
    <h4>Latest Tweet`s</h4>
    <p style="padding-left:14px">Praesent convallis placerat lorem, quis tincidunt lorem feugiat ut. Morbi ac purus consectetur purus blandit <a>vehicula non</a> a dolor. Mauris quis lacus ut purus sodales pharetra.</p>
    <p style="padding-left:14px;margin-top:6px">Feb -23, 2015</p>
  </div>
  <div class="fsep" style="left:550px"></div>
  <div class="col" style="left:576px">
    <h4>Quick Links</h4>
    <ul class="links"><li>Home</li><li>Services</li><li>Expertise</li><li>About Us</li><li>Press</li><li>Contact</li></ul>
  </div>
  <div class="fsep" style="left:665px"></div>
  <div class="col" style="left:685px">
    <h4>Newsletter</h4>
    <div class="email">E-mail<span><svg width="9" height="10" viewBox="0 0 9 10"><path d="M0 0l9 5-9 5z" fill="#666"/></svg></span></div>
    <h4 style="margin-top:12px">Follow us on</h4>
    <div class="social"><i></i><i></i></div>
  </div>
</footer>

<div class="section bottom">
  <p style="top:20px">Copyright © 2015 &nbsp;Keystone Public Relations. All Rights Reserved.</p>
  <p style="top:39px">Disclaimer &nbsp;| &nbsp;Support &nbsp;| &nbsp;Privacy Policy &nbsp;| &nbsp;Terms of use</p>
  <div class="bottom-icons">
    <svg width="21" height="21" viewBox="0 0 21 21"><circle cx="10.5" cy="10.5" r="9.5" fill="none" stroke="#ccc" stroke-width="1.2"/><circle cx="10.5" cy="10.5" r="6" fill="#fff"/><path d="M7.5 8.5h6v4h-6zM7.5 8.5l3 2 3-2" fill="none" stroke="#141414" stroke-width=".9"/></svg>
    <svg width="21" height="21" viewBox="0 0 21 21"><circle cx="10.5" cy="10.5" r="9.5" fill="none" stroke="#888" stroke-width="1.2"/><path d="M10.5 15V6M7 9.5l3.5-3.5 3.5 3.5" fill="none" stroke="#888" stroke-width="1.4"/></svg>
  </div>
</div>

</body>
</html>
```